Business Card & Logo Design for a communications based company

I am looking for a business card and logo design for a communications based company.. We specialize in Fiber Optics
I have an image i would like to use towards the logo which i have uploaded. (Use of the image is totally up to you the designers)
Background color - Blue OR Black. (thats just my preference..Use of those colors are totally up to the designer)
Text -
Company Name - Brisa Networks LTD
Name - Marcel Dostiwana
Contact Number - (555) 417-2904
Adress - Palmview Heights
Company Motto - Stay Connected !
Services Offered
Fiber Optic Solutions
Full Networking Solutions
IP Surveillance Systems
Access Control Systems
Alarms
Industry/Entity Type
Communications
Contact Information for Business Card
Text -
Name - Marcel Dostiwana
Adress - Palmview Heights
Services Offered
Fiber Optic Solutions
Full Networking Solutions
IP Surveillance Systems
Access Control Systems
Alarms

```html
<!DOCTYPE html>
<html lang="en">
<head>
<meta charset="utf-8">
<title>Brisa Networks LTD – Business Card</title>
<link href="https://fonts.googleapis.com/css2?family=Hind:wght@500;600&display=swap" rel="stylesheet">
<style>
  :root {
    --ink: #070707;
    --paper: #ffffff;
  }
  html, body {
    margin: 0;
    padding: 0;
    width: 1200px;
    height: 632px;
    overflow: hidden;
    background: var(--ink);
  }
  .card {
    position: relative;
    width: 1200px;
    height: 632px;
    background: var(--ink);
    font-family: "Hind", "Segoe UI", sans-serif;
    color: var(--paper);
  }
  .company-name {
    position: absolute;
    left: 281px;
    top: 33px;
    margin: 0;
    font-size: 61px;
    font-weight: 600;
    line-height: 1;
    letter-spacing: 0.2px;
    white-space: nowrap;
  }
  .motto {
    position: absolute;
    left: 285px;
    top: 96px;
    margin: 0;
    font-size: 44px;
    font-weight: 600;
    line-height: 1;
    white-space: nowrap;
  }
  .header-rule {
    position: absolute;
    left: 248px;
    right: 0;
    top: 179px;
    height: 3px;
    background: var(--paper);
  }
  .contact-frame {
    position: absolute;
    left: 595px;
    right: 0;
    top: 348px;
    height: 244px;
    background: var(--paper);
  }
  .contact-panel {
    position: absolute;
    left: 650px;
    right: 0;
    top: 382px;
    height: 196px;
    background: var(--ink);
  }
  .contact-divider {
    position: absolute;
    left: 712px;
    top: 406px;
    width: 2px;
    height: 147px;
    background: var(--paper);
  }
  .contact-details {
    position: absolute;
    left: 740px;
    width: 436px;
    top: 408px;
    margin: 0;
    text-align: center;
    font-size: 44px;
    font-weight: 500;
    line-height: 48px;
    white-space: nowrap;
  }
  .contact-details span { display: block; }
</style>
</head>
<body>
  <div class="card">
    <h1 class="company-name">Brisa Networks LTD</h1>
    <p class="motto">Stay Connected !</p>
    <div class="header-rule"></div>

    <div class="contact-frame"></div>
    <div class="contact-panel"></div>
    <div class="contact-divider"></div>
    <p class="contact-details">
      <span class="contact-name">Marcel Dostiwana</span>
      <span class="contact-phone">(555) 417-2904</span>
      <span class="contact-area">Palmview Heights</span>
    </p>
  </div>
</body>
</html>
```